Home Security Website

This website is for a home security website. We feature the best in home security products and monitoring. The website name is Hearthwise Crew.
We would like a direct response design with a large hero image.
The final design should incorporate safety, security, and family. Please do not use scare tactics in the design.
Target Market(s)
Women, primarily
Industry/Entity Type
Security
Requirements
Must have
- Must have a clear Call to Action Area for telephone and lead gen form
Nice to have
- - Large heroes with lifestyle images of family - security
- below the fold text area with boxes
Should not have
- no scare tactics please
DO NOT submit designs with DARK or BLACK backgrounds

```html
<!DOCTYPE html>
<html lang="en">
<head>
<meta charset="utf-8">
<title>Hearthwise Crew</title>
<link href="https://fonts.googleapis.com/css2?family=Roboto+Condensed:wght@400;700&family=Anton&family=Arimo:wght@400;700&display=swap" rel="stylesheet">
<style>
:root{
  --blue:#0b97dc;
  --blue-dark:#0779b5;
  --red:#c4121a;
  --grey-band:#666666;
  --grey-btn:#5e5e5e;
  --text:#6b6b6b;
  --brown:#7a4a2c;
  --orange:#f5a40f;
  --white:#ffffff;
}
*{margin:0;padding:0;box-sizing:border-box}
html,body{width:938px;height:1200px;overflow:hidden;background:var(--white)}
body{position:relative;font-family:"Arimo",sans-serif;color:var(--text)}
.abs{position:absolute}

.topbar{left:0;top:0;width:938px;height:38px;background:var(--blue);border-bottom:3px solid #3fb3ea}
.navbar{left:0;top:41px;width:938px;height:29px;background:linear-gradient(#ffffff,#e9e9e9);border-bottom:1px solid #d5d5d5}
.brand-tab{left:102px;top:0;width:73px;height:88px;background:var(--white);box-shadow:0 1px 3px rgba(0,0,0,.25);z-index:3}
.brand-mark{left:22px;top:20px;width:30px;height:30px;background:var(--red)}
.brand-name{left:196px;top:9px;font-family:"Roboto Condensed",sans-serif;font-weight:700;font-size:21px;color:var(--white);letter-spacing:-.3px}
.search{left:620px;top:11px;width:158px;height:19px;background:var(--blue-dark);border-radius:3px;border:1px solid #0a86c4;font-family:"Roboto Condensed",sans-serif;font-size:10px;color:#cfe9f7;padding:3px 6px}
.search svg{position:absolute;right:6px;top:3px}
.login{left:787px;top:11px;width:48px;height:19px;background:var(--red);border-radius:2px;color:var(--white);font-family:"Roboto Condensed",sans-serif;font-weight:700;font-size:11px;text-align:center;line-height:19px}
.nav a{position:absolute;top:49px;font-family:"Roboto Condensed",sans-serif;font-size:11px;color:var(--blue);text-decoration:none;line-height:15px}
.nav a.current{background:var(--grey-btn);color:var(--white);padding:0 5px;border-radius:2px;left:196px}

.hero{left:0;top:70px;width:938px;height:467px;background:linear-gradient(100deg,#a99e8a 0%,#d8d2c2 35%,#e7e0a8 60%,#c9a46e 80%,#b7a383 100%)}
.band{left:0;top:537px;width:938px;height:165px;background:var(--grey-band);border-bottom:3px solid #cfcfcf}

.ribbon{font-family:"Anton",sans-serif;color:var(--white);letter-spacing:.5px;line-height:1;text-shadow:1px 2px 2px rgba(0,0,0,.35)}
.r1{left:100px;top:338px;width:153px;height:66px;background:linear-gradient(#8a5533,#6a3e22);font-size:40px;padding:12px 0 0 16px}
.r1-tail{left:76px;top:342px}
.r2{left:112px;top:414px;width:191px;height:63px;background:linear-gradient(#159ad6,#0a78b6);font-size:40px;padding:11px 0 0 12px}
.r3{left:126px;top:490px;width:392px;height:62px;background:linear-gradient(#ffb81b,#f29a06);font-size:40px;padding:10px 0 0 14px}
.r3-tail{left:512px;top:494px}

.welcome-title{left:104px;top:570px;font-family:"Arimo",sans-serif;font-weight:700;font-size:35px;color:var(--white);letter-spacing:.5px}
.welcome-box{left:102px;top:620px;width:484px;height:190px;background:linear-gradient(#ffffff,#f4f4f4);border:1px solid #d8d8d8;padding:20px 16px;font-size:8.4px;line-height:10.4px}
.welcome-box p{margin-bottom:7px}
.notch{left:112px;top:612px}

.callout{left:603px;top:470px;width:232px;height:340px;background:linear-gradient(#ffffff,#f6f6f6);border:1px solid #d5d5d5}
.call-now{left:0;top:0;width:230px;height:34px;font-family:"Anton",sans-serif;font-size:26px;color:#555;text-align:center;line-height:36px;letter-spacing:1px}
.call-number{left:-1px;top:34px;width:232px;height:38px;background:linear-gradient(#d01a22,#a80d13);font-family:"Anton",sans-serif;color:var(--white);font-size:29px;line-height:38px;padding-left:40px}
.call-number svg{position:absolute;left:14px;top:9px}
.field{position:absolute;left:12px;width:207px;height:23px;border:1px solid #cfcfcf;background:var(--white);font-size:9px;color:#aaa;padding:5px 8px}
.submit{left:155px;top:304px;width:64px;height:24px;background:linear-gradient(#d01a22,#a80d13);border:1px solid #8a0a0f;font-family:"Anton",sans-serif;color:var(--white);font-size:16px;text-align:center;line-height:23px}

.feature{top:840px;width:228px}
.feature h2{font-family:"Roboto Condensed",sans-serif;font-weight:400;font-size:21px;color:var(--blue);margin-bottom:5px}
.feature p{font-size:8.4px;line-height:10.5px;height:110px}
.read-more{display:inline-block;margin-top:19px;width:61px;height:20px;background:var(--grey-btn);border:1px solid #444;color:var(--white);font-weight:700;font-size:8.5px;text-align:center;line-height:18px}

.product{top:1036px;height:88px;text-align:center}
.product+.product{border-left:1px solid #d8d8d8}
.product h3{font-family:"Roboto Condensed",sans-serif;font-weight:700;font-size:10.5px;color:var(--blue);letter-spacing:.2px}
.product .thumb{margin:14px auto 0;width:78px;height:58px;border-radius:6px;background:linear-gradient(#f1f1f1,#d9d9d9)}
.product .thumb.dark{background:linear-gradient(#6a7fb5,#2c3f7a);width:60px;border-radius:20px}

.footer{left:0;top:1157px;width:938px;height:43px;background:var(--blue);color:var(--white);font-size:8.6px}
.footer .copy{left:102px;top:16px}
.footer .links{right:106px;top:16px}
</style>
</head>
<body>

<header>
  <div class="abs topbar"></div>
  <div class="abs navbar"></div>
  <div class="abs brand-tab"><div class="abs brand-mark"></div></div>
  <div class="abs brand-name">Hearthwise Crew</div>
  <div class="abs search">SEARCH
    <svg width="12" height="12" viewBox="0 0 12 12"><circle cx="7" cy="5" r="3.5" fill="none" stroke="#cfe9f7" stroke-width="1.5"/><line x1="4.5" y1="7.5" x2="1" y2="11" stroke="#cfe9f7" stroke-width="2"/></svg>
  </div>
  <div class="abs login">LOGIN</div>
  <nav class="nav">
    <a class="current" href="#">HOME</a>
    <a href="#" style="left:251px">ALARM SYSTEMS</a>
    <a href="#" style="left:353px">HOME AUTOMATION</a>
    <a href="#" style="left:470px">ENVIRONMENT CONTROLS</a>
    <a href="#" style="left:614px">CHILD SAFETY</a>
    <a href="#" style="left:700px">ABOUT US</a>
    <a href="#" style="left:771px">CONTACT US</a>
  </nav>
</header>

<section>
  <div class="abs hero" role="img" aria-label="Family at home smiling as the father sets the wall-mounted security control panel"></div>
  <div class="abs band"></div>

  <svg class="abs r1-tail" width="30" height="62" viewBox="0 0 30 62"><polygon points="0,0 30,0 30,62 0,62 12,31" fill="#5c3520"/></svg>
  <div class="abs ribbon r1">LET US</div>
  <div class="abs ribbon r2">HELP YOU</div>
  <svg class="abs r3-tail" width="32" height="62" viewBox="0 0 32 62"><polygon points="0,0 32,0 20,31 32,62 0,62" fill="#e48a05"/></svg>
  <div class="abs ribbon r3">PROTECT YOUR HOME</div>

  <h1 class="abs welcome-title">Welcome</h1>
  <svg class="abs notch" width="18" height="9" viewBox="0 0 18 9"><polygon points="0,9 9,0 18,9" fill="#fff"/></svg>
  <div class="abs welcome-box">
    <p>Mauris id turpis nec quam scelerisque molestie. Nam ornare ante vel leo bibendum malesuada. Pellentesque consectetur interdum euismod. Nunc facilisis nibh eu nisi viverra sit amet auctor justo tincidunt. Aenean vulputate magna non ipsum feugiat eneanenean vulputate magna non ipsum feugiat vulputate magna non ipsum feugiat pulvinar non vitae nibh. In hac habitasse platea dictumst. Vivamus non egestas odio.</p>
    <p>Sed at velit nisl. In bibendum, sapien id congue venenatis, metus diam ultrices nunc, eu rhoncus lorem risus mollis mi. Ut interdum tincidunt convallis. Aenean non urna augue, at dignissim odio. Vivamus vulputate neque quis tellus interdum tempor. Phasellus vel enim lectus, in pellentesque elit. Nunc tincidunt, nisi in luctus feugiat, Phasellus vel enim lectus, in pellentesque elit. Nunc tincidunt, nisi in luctus feugiat, dui lacus tristique turpis, nec auctor nisi nulla quis est. Donec non dictum diam. Duis feugiat molestie ultricies.</p>
    <p>Mauris id turpis nec quam scelerisque molestie. Nam ornare ante vel leo bibendum malesuada. Pellentesque consectetur interdum euismod. Nunc facilisis nibh eu nisi viverra sit amet auctor justo tincidunt. Aenean vulputate magna non ipsum feugiat eneanenean vulputate magna non ipsum feugiat vulputate magna non ipsum feugiat pulvinar non vitae nibh. In hac habitasse platea dictumst. Vivamus non egestas odio.</p>
  </div>

  <aside class="abs callout">
    <div class="abs call-now">CALL NOW</div>
    <div class="abs call-number">
      <svg width="20" height="20" viewBox="0 0 20 20"><path d="M4 1 L8 1 L9 6 L6.5 8 C8 11 9.5 12.5 12 14 L14 11.5 L19 12.5 L19 16.5 C19 18 18 19 16.5 19 C8 18.5 1.5 12 1 3.5 C1 2 2 1 4 1 Z" fill="#fff"/></svg>
      800-555-0142
    </div>
    <div class="field" style="top:84px">First Name</div>
    <div class="field" style="top:118px">Last Name</div>
    <div class="field" style="top:153px">Email Address</div>
    <div class="field" style="top:188px;height:103px">Message</div>
    <div class="abs submit">SUBMIT</div>
  </aside>
</section>

<section>
  <div class="abs feature" style="left:102px">
    <h2>Alarm Systems</h2>
    <p>Mauris id turpis nec quam scelerisque molestie. Nam ornare ante vel leo bibendum malesuada. Pellentesque consectetur interdum euismod. Nunc facilisis nibh eu nisi viverra sit amet auctor justo tincidunt. non ipsum feugiat pulvinar non vitae nibh. In hac Aenean vulputate magna non ipsum feugiat eneanenean vulputate magna non ipsum feugiat vulputate magna non ipsum feugiat pulvinar non vitae nibh. In hac non ipsum feugiat pulvinar non vitae nibh. In hac habitasse platea dictumst. Vivamus non egestas odio.</p>
    <span class="read-more">Read More</span>
  </div>
  <div class="abs feature" style="left:347px">
    <h2>Home Automation</h2>
    <p>Sed at velit nisl. In bibendum, sapien id congue venenatis, metus diam ultrices nunc, eu rhoncus lorem risus mollis mi. Ut interdum tincidunt convallis. Aenean non urna augue, at dignissim odio. Vivamus vulputate neque quis tellus interdum tempor. Phasellus vel enim lectus, in pellentesque elit. Nunc tincidunt, nisi in luctus feugiat, Phasellus vel enim lectus, in pellentesque elit. Nunc tincidunt, nisi in luctus feugiat, dui lacus tristique turpis, nec auctor nisi nulla quis est. Donec non dictum diam. Duis feugiat molestie ultricies.</p>
    <span class="read-more">Read More</span>
  </div>
  <div class="abs feature" style="left:592px">
    <h2>Environmental Controls</h2>
    <p>Mauris id turpis nec quam scelerisque molestie. Nam ornare ante vel leo bibendum malesuada. Pellentesque consectetur interdum euismod. Nunc facilisis nibh eu nisi viverra sit amet auctor justo tincidunt. non ipsum feugiat pulvinar non vitae nibh. In hac Aenean vulputate magna non ipsum feugiat eneanenean vulputate magna non ipsum feugiat vulputate magna non ipsum feugiat pulvinar non vitae nibh. In hac non ipsum feugiat pulvinar non vitae nibh. In hac habitasse platea dictumst. Vivamus non egestas odio.</p>
    <span class="read-more">Read More</span>
  </div>
</section>

<section>
  <div class="abs product" style="left:100px;width:110px"><h3>WIRELESS ALARMS</h3><div class="thumb" role="img" aria-label="Wireless alarm kit with keypad and sensors"></div></div>
  <div class="abs product" style="left:210px;width:124px"><h3>HARDWARE ALARMS</h3><div class="thumb" role="img" aria-label="Wired alarm panel and keypad"></div></div>
  <div class="abs product" style="left:334px;width:124px"><h3>SECURITY CAMERAS</h3><div class="thumb" role="img" aria-label="Outdoor security camera on a bracket"></div></div>
  <div class="abs product" style="left:458px;width:120px"><h3>DRIVEWAY ALARMS</h3><div class="thumb" role="img" aria-label="Driveway motion sensor and receiver"></div></div>
  <div class="abs product" style="left:578px;width:144px"><h3>PERSONAL PROTECTION</h3><div class="thumb dark" role="img" aria-label="Handheld personal protection device"></div></div>
  <div class="abs product" style="left:722px;width:116px"><h3>EXCLUSIVE BUNDLES</h3><div class="thumb" role="img" aria-label="Bundle of alarm devices and accessories"></div></div>
</section>

<footer class="abs footer">
  <div class="abs copy">Copyright © 2013 Hearthwise Crew. All Rights Reserved. User Agreement and Privacy Policy.</div>
  <div class="abs links">About Us &nbsp;| &nbsp;Contact Us &nbsp;| Sitemap</div>
</footer>

</body>
</html>
```